Bottle label design for a mulberry brandy

Please create a label design for a mulberry brandy. The registered brand name is "Kolvat"
The brandy will be produced in Armenia from 100% mulberry.
Color of the product: transparent.
The product will be sold worldwide. The price will be between 30 and 50 USD. So the product will be in premium category.
Therefore we need a solid design, appropriate to the product price category. The design, however, needs to be modern and optimistic.
You can have mulberries on the label or not have, it is up to you.
We have chosen for the product some bottle types, the links to the available bottles you can find in the attachment. Ideally you show a picture of your label on the bottle you selected.

Target Market(s)

worldwide

```html
<!DOCTYPE html>
<html lang="en">
<head>
<meta charset="utf-8">
<title>Kolvat Mulberry Brandy – Label</title>
<link rel="stylesheet" href="https://fonts.googleapis.com/css2?family=Playfair+Display+SC:wght@700&family=Oswald:wght@500&display=swap">
<style>
  :root {
    --page-bg: #ffffff;
    --navy-deep: #14205a;
    --royal-blue: #2e4fa6;
    --sky-blue: #7fa8dc;
    --pale-blue: #d9e5f4;
    --paper: #f7f9fc;
    --berry: #5b6a86;
    --ink-light: #ffffff;
  }
  html, body {
    margin: 0;
    padding: 0;
    overflow: hidden;
    background: var(--page-bg);
  }
  .canvas {
    position: relative;
    width: 1066px;
    height: 1200px;
    background: var(--page-bg);
    overflow: hidden;
  }
  .label {
    position: absolute;
    left: 198px;
    top: 100px;
    width: 670px;
    height: 1000px;
  }
  .label__outer { fill: var(--royal-blue); }
  .label__frame { fill: url(#frameTone); }
  .label__field { fill: url(#fieldTone); }
  .label__banner { fill: var(--navy-deep); stroke: var(--ink-light); stroke-width: 4; }
  .label__banner-rule { fill: none; stroke: var(--sky-blue); stroke-width: 2; }
  .label__berries { fill: var(--berry); }
  .label__brand {
    font-family: "Playfair Display SC", "Times New Roman", serif;
    font-weight: 700;
    font-size: 96px;
    letter-spacing: 2px;
    fill: var(--ink-light);
  }
  .label__product {
    font-family: "Oswald", "Arial Narrow", sans-serif;
    font-weight: 500;
    font-size: 20px;
    letter-spacing: 2px;
    fill: var(--ink-light);
  }
</style>
</head>
<body>
<div class="canvas">
  <svg class="label" viewBox="0 0 670 1000" xmlns="http://www.w3.org/2000/svg">
    <defs>
      <linearGradient id="frameTone" x1="0" y1="0" x2="0" y2="1">
        <stop offset="0" stop-color="#e6eef8"/>
        <stop offset="0.5" stop-color="#f7f9fc"/>
        <stop offset="1" stop-color="#dbe6f4"/>
      </linearGradient>
      <linearGradient id="fieldTone" x1="0" y1="0" x2="0" y2="1">
        <stop offset="0" stop-color="#5f8fd0"/>
        <stop offset="0.5" stop-color="#8fb4e2"/>
        <stop offset="1" stop-color="#5f8fd0"/>
      </linearGradient>
    </defs>

    <polygon class="label__outer"
      points="30,0 640,0 640,30 670,30 670,970 640,970 640,1000 30,1000 30,970 0,970 0,30 30,30"/>

    <polygon class="label__frame" role="img" aria-label="Art deco sunburst line rays framing the label"
      points="48,18 622,18 622,48 652,48 652,952 622,952 622,982 48,982 48,952 18,952 18,48 48,48"/>

    <polygon class="label__field" role="img" aria-label="Blue art deco scale pattern"
      points="90,140 580,140 525,500 580,860 90,860 145,500"/>

    <rect class="label__berries" role="img" aria-label="Small mulberry cluster illustration"
      x="305" y="232" width="60" height="38" rx="16"/>

    <polygon class="label__banner"
      points="55,440 335,372 615,440 615,522 335,590 55,522"/>
    <polygon class="label__banner-rule"
      points="75,450 335,392 595,450 595,512 335,570 75,512"/>

    <text class="label__brand" x="335" y="515" text-anchor="middle">Kolvat</text>

    <text class="label__product" x="335" y="775" text-anchor="middle">MULBERRY BRANDY</text>
  </svg>
</div>
</body>
</html>
```